Tamarack Hearth Partners Business Card

Looking for a new business card layout. We are a real estate firm w/ a logo, old design attached. Must keep the same elements on there, just need a fresh look and possible some foil accents. Looking for a simpler design w/ more modern style.

Target Market(s)

Real Estate clients

Industry/Entity Type

Real Estate Agent

Contact Information for Business Card

see attached

Font styles to use
Sans Serif

Requirements
Must have
• all elements on current biz card
Nice to have
• modern look, simpler than we have!
Should not have
• no serif fonts

```html
<!DOCTYPE html>
<html lang="en">
<head>
<meta charset="utf-8">
<title>Tamarack Hearth Partners Business Card</title>
<link href="https://fonts.googleapis.com/css2?family=Questrial&display=swap" rel="stylesheet">
<style>
  :root {
    --page: #f7f7f7;
    --card: #000000;
    --silver: #c4c4c4;
    --silver-light: #dcdcdc;
    --text: #d6d6d6;
    --photo-top: #d9c6a6;
    --photo-bottom: #2bb7bf;
  }
  * { margin: 0; padding: 0; box-sizing: border-box; }
  html, body { width: 1200px; height: 1200px; overflow: hidden; }
  body {
    background: var(--page);
    font-family: "Questrial", "Century Gothic", sans-serif;
    position: relative;
  }
  .card {
    position: absolute;
    top: 453px;
    width: 514px;
    height: 294px;
    background: var(--card);
  }
  .card--front { left: 68px; }
  .card--back { left: 618px; }

  .agent-photo {
    position: absolute;
    left: 70px; top: 44px;
    width: 113px; height: 152px;
    border-radius: 6px;
    background: linear-gradient(180deg, var(--photo-top) 0%, #c9a57a 50%, var(--photo-bottom) 100%);
  }
  .agent-name {
    position: absolute;
    left: 0; width: 250px;
    top: 216px;
    text-align: center;
    color: var(--silver-light);
    font-size: 36px;
    line-height: 1;
  }
  .agent-title {
    position: absolute;
    left: 0; width: 250px;
    top: 256px;
    text-align: center;
    color: var(--text);
    font-size: 12px;
  }
  .divider {
    position: absolute;
    left: 243px; top: 175px;
    width: 2px; height: 100px;
    background: var(--silver-light);
  }

  .brand-name {
    color: var(--silver);
    text-transform: uppercase;
    letter-spacing: 1.5px;
    line-height: 1.15;
  }
  .card--front .brand-name {
    position: absolute;
    left: 292px; top: 26px;
    font-size: 18px;
  }
  .card--back .brand-name {
    position: absolute;
    left: 0; right: 0; top: 112px;
    text-align: center;
    font-size: 28px;
  }

  .contact-list {
    position: absolute;
    left: 287px; top: 172px;
    list-style: none;
    color: var(--text);
    font-size: 12.5px;
    line-height: 1.2;
  }
  .contact-item {
    display: flex;
    align-items: flex-start;
    margin-bottom: 3px;
  }
  .contact-item svg {
    width: 11px; height: 11px;
    margin-right: 12px;
    margin-top: 2px;
    flex: none;
    fill: var(--silver);
  }
</style>
</head>
<body>
  <section class="card card--front">
    <div class="agent-photo" role="img" aria-label="Portrait photo of the agent"></div>
    <div class="agent-name">Marin Vale</div>
    <div class="agent-title">Principal Broker</div>
    <div class="divider"></div>

    <div class="brand-name">Tamarack Hearth<br>Partners</div>

    <ul class="contact-list">
      <li class="contact-item">
        <svg viewBox="0 0 12 12"><path d="M6 0a4 4 0 0 0-4 4c0 3 4 8 4 8s4-5 4-8a4 4 0 0 0-4-4zm0 5.5A1.5 1.5 0 1 1 6 2.5a1.5 1.5 0 0 1 0 3z"/></svg>
        <span>218 NE Alder St<br>Pinecrest, OR 97700</span>
      </li>
      <li class="contact-item">
        <svg viewBox="0 0 12 12"><path d="M1 4c0-2 2-3 5-3s5 1 5 3v1H8.5V3.8h-5V5H1zM3 6h6l1.5 5h-9z"/></svg>
        <span>541.555.0142</span>
      </li>
      <li class="contact-item">
        <svg viewBox="0 0 12 12"><path d="M3 0h6v12H3zM4 1v8.5h4V1zM5.5 10.2h1v1h-1z" fill-rule="evenodd"/></svg>
        <span>541.555.0187</span>
      </li>
      <li class="contact-item">
        <svg viewBox="0 0 12 12"><path d="M0 2.5h12v7H0zM0.8 3.2 6 7l5.2-3.8"/></svg>
        <span>marin@tamarackhearth.com</span>
      </li>
      <li class="contact-item">
        <svg viewBox="0 0 12 12"><circle cx="6" cy="6" r="5.5"/><path d="M0.5 6h11M6 0.5v11M2 3h8M2 9h8" stroke="#000" stroke-width="0.8" fill="none"/></svg>
        <span>TamarackHearth-Homes.com</span>
      </li>
    </ul>
  </section>

  <section class="card card--back">
    <div class="brand-name">Tamarack Hearth<br>Partners</div>
  </section>
</body>
</html>
```